Flyer for annual KESTREL SUMMIT 2020

I would like a church event flyer designed. The event is called "KESTREL SUMMIT 2020". I am looking for a professional, yet catchy design that uses our brand colors and logo creatively while communicating key information of the event effectively.

1. The logo is attached in two color formats. The designer has the choice to use them as he/she want.

2. The location of the event is: Harlow Community Center, 239 Fennimore Street, Portland, ME 04117

3. Time and date of event. The designer can organize and format the date and time as he/she pleases.
Thursday December 31st @ 6:30PM
Friday January 1st @ 6:30PM
Saturday 2nd @ 6:30PM
Sunday 3rd @ 4:30PM

4. The topic of the event is "In Fire and On Fire". The designer is free to use this phrase as he/she pleases to create a good composition.

5. Speaker: Prophet Marcus Olunde (2 pictures of the speaker to choose from are attached)

6. Contact information: contact@brightmeadowfold.org - Telephone number: 207 583 2914

7. I would also like the following three words on the flyer. These words describe the focus of the event: FIRE, REVIVAL, PROPHETIC

Target Market(s)

Young adults

Font styles to use
Sans Serif

Requirements
Must have
• Logo, speaker's picture
Should not have
• cross image, church image

```html
<!DOCTYPE html>
<html lang="en">
<head>
<meta charset="utf-8">
<title>Kestrel Summit 2020 Flyer</title>
<link href="https://fonts.googleapis.com/css2?family=Cinzel:wght@400;500;600&family=Arimo:wght@400&display=swap" rel="stylesheet">
<style>
  :root {
    --page-bg: #ececec;
    --purple-deep: #2a1840;
    --purple-mid: #3d2558;
    --purple-light: #5a3e78;
    --gold: #d9b27f;
    --gold-light: #f3dcc0;
    --gold-dark: #a8794a;
    --cream: #f4e9dd;
    --white: #ffffff;
    --suit: #d2532e;
  }
  * { margin: 0; padding: 0; box-sizing: border-box; }
  html, body { width: 1200px; height: 776px; overflow: hidden; background: var(--page-bg); }
  .flyer {
    position: absolute; left: 338px; top: 18px; width: 524px; height: 740px; overflow: hidden;
    background: linear-gradient(180deg, var(--purple-light) 0%, var(--purple-mid) 35%, var(--purple-deep) 100%);
    font-family: "Cinzel", serif; color: var(--cream);
  }
  .speaker-photo { position: absolute; left: 212px; top: 16px; width: 236px; height: 372px;
    background: linear-gradient(180deg, #4a2e3a 0%, #b5482a 40%, var(--suit) 100%); }
  .flame-area { position: absolute; left: 392px; top: 378px; width: 132px; height: 362px;
    background: linear-gradient(180deg, rgba(243,220,192,0.15) 0%, rgba(217,178,127,0.75) 45%, rgba(168,121,74,0.85) 100%); }
  .flyer-art { position: absolute; inset: 0; }
  .brand { position: absolute; left: 42px; top: 58px; display: flex; align-items: center; gap: 8px; }
  .brand-mark { width: 14px; height: 14px; border-radius: 50%; background: var(--gold); }
  .brand-name { font-size: 32px; font-weight: 500; color: var(--white); letter-spacing: 1px; line-height: 1; }
  .event-title { position: absolute; left: 10px; width: 214px; top: 124px; text-align: center; color: var(--gold); font-weight: 400; line-height: 1; }
  .event-title .line { display: block; font-size: 26px; letter-spacing: 1px; }
  .event-title .line + .line { margin-top: 5px; }
  .event-title .year { display: block; font-size: 66px; margin-top: 2px; color: var(--gold-light); }
  .speaker-label { position: absolute; left: 39px; top: 261px; width: 143px; height: 26px; border-radius: 13px;
    background: linear-gradient(90deg, var(--gold-dark), var(--gold-light), var(--gold-dark));
    color: var(--purple-deep); font-size: 17px; font-weight: 600; text-align: center; line-height: 26px; }
  .speaker-name { position: absolute; left: 6px; width: 210px; top: 295px; text-align: center; font-size: 20px; line-height: 25px; color: var(--cream); }
  .schedule { position: absolute; left: 21px; top: 368px; list-style: none; }
  .schedule li { display: flex; align-items: center; height: 40.5px; }
  .schedule .num { width: 30px; height: 30px; border: 1.5px solid var(--cream); border-radius: 50%;
    text-align: center; line-height: 27px; font-size: 16px; margin-right: 16px; }
  .schedule .when { font-family: "Arimo", sans-serif; font-size: 7.5px; line-height: 9.5px; color: var(--cream); }
  .focus-words { position: absolute; left: 160px; top: 421px; width: 200px; text-align: center; font-size: 27px; font-weight: 500; line-height: 30px; color: var(--cream); }
  .contact { position: absolute; left: 160px; width: 210px; top: 620px; text-align: center; }
  .contact-heading { font-size: 13px; color: var(--gold-light); letter-spacing: 0.5px; }
  .contact-detail { font-family: "Arimo", sans-serif; font-size: 13px; line-height: 19px; color: var(--white); }
  .contact-heading + .contact-detail { margin-top: 8px; }
  .venue { position: absolute; left: 94px; top: 698px; width: 342px; height: 24px; border-radius: 12px;
    border: 1px solid var(--cream); background: linear-gradient(90deg, var(--gold-dark), var(--gold), var(--gold-dark));
    font-family: "Arimo", sans-serif; font-size: 9.5px; text-align: center; line-height: 22px; color: var(--white); }
</style>
</head>
<body>
<main class="flyer">
  <div class="speaker-photo" role="img" aria-label="Photo of the speaker, Prophet Marcus Olunde, in an orange suit"></div>
  <div class="flame-area" role="img" aria-label="Large gold flame illustration for the theme In Fire and On Fire"></div>

  <svg class="flyer-art" width="524" height="740" viewBox="0 0 524 740" aria-hidden="true">
    <defs>
      <linearGradient id="gold-sweep" x1="0" y1="0" x2="1" y2="0">
        <stop offset="0" stop-color="#a8794a"/>
        <stop offset="0.5" stop-color="#f3dcc0"/>
        <stop offset="1" stop-color="#c9965f"/>
      </linearGradient>
    </defs>
    <path d="M0 578 C160 572 330 420 524 324 C340 398 190 560 0 588 Z" fill="url(#gold-sweep)"/>
    <circle cx="260" cy="468" r="112" fill="#2e1b46"/>
    <circle cx="260" cy="468" r="106" fill="none" stroke="url(#gold-sweep)" stroke-width="9"/>
  </svg>

  <div class="brand">
    <span class="brand-mark"></span>
    <span class="brand-name">HALVERN</span>
  </div>

  <h1 class="event-title">
    <span class="line">KESTREL</span>
    <span class="line">SUMMIT</span>
    <span class="year">2020</span>
  </h1>

  <div class="speaker-label">SPEAKER</div>
  <p class="speaker-name">Prophet<br>Marcus Olunde</p>

  <ul class="schedule">
    <li><span class="num">1</span><span class="when">THURSDAY<br>December 31st<br>6:30PM</span></li>
    <li><span class="num">2</span><span class="when">FRIDAY<br>January 1st<br>6:30PM</span></li>
    <li><span class="num">3</span><span class="when">SATURDAY<br>January 2nd<br>6:30PM</span></li>
    <li><span class="num">4</span><span class="when">SUNDAY<br>January 3rd<br>4:30PM</span></li>
  </ul>

  <p class="focus-words">FIRE<br>REVIVAL<br>PROPHETIC</p>

  <div class="contact">
    <p class="contact-heading">CONTACT US</p>
    <p class="contact-detail">207 583 2914</p>
    <p class="contact-detail">contact@brightmeadowfold.org</p>
  </div>

  <p class="venue">Harlow Community Center, 239 Fennimore Street, Portland, ME 04117</p>
</main>
</body>
</html>
```